Label / Packaging design for supplements bottle (capsule bottle)

We are a startup supplements company focusing on animal nutrition. The task here is to design the supplement bottles for the product series. Think of bodybuilding supplement packaging more than health&wellness type of packaging.

The brandname is Roost Vector

The goal is to have 3 bottles with similar/identical designs but with different color accents (i.e. red for one bottle, yellow for the second, (not green or blue) for the third).

The bottles can either be black theme or white theme. I'll leave it up to the designer.

Final design should communicate bodybuilding (bold fonts preferred)

Logo files below (both SVG and AI files), the insignia can be used independently of the text and slogan, or it can be positioned above brand name or beside it.
*Feel free to change the color of the insignia and text to match your chosen accent color for the bottle!*

Bottle size will be approximately 11.9cm x 6.35cm (Height x circumference) (height is from bottom to mouth opening)
Thus, label size at the moment can be designed 6.30cm x 10cm (L x W)

Target Market(s)

Male, Adult

Industry/Entity Type

It Company

Font styles to use
Sans Serif

Requirements
Must have
• Text: "Performance Enhancing Supplements for Racing Pigeons"
• Essentials
• "240 Capsules"
• Bottle 1:
• Creatine+Carnitine
• Text + Imagery:*see Carnitine Benefits.png
• Bottle 2:
• BCAA
• Text:
• SUPPORT MUSCLE PROTEIN SYNTHESIS
• DECREASE PROTEIN CATABOLISM
• PROMOTE INSULIN SENSITIVITY
• Offset Muscle Breakdown and Increase Muscular Endurance
• ENHANCED RECOVERY FROM EXERCISE
• Promotes Lowered Body Fat Levels, Increased Strength, & Improves Muscle Repair
• (Imagery can use the same as bottle 1 similar to Carnitine Benefits.png)
• Bottle 3:
• Vitamins
• Text: Supports Rigorous Training and Needs To Support Growth and Overall Well-being
• Spaces for Text for:
• 1.) Directions for Use
• 2.) Developed by:
• 3.) Ingredients
Nice to have
• Mosaic/Pattern subtle fading background (e.g. honeycomb etc)
• Prominent "A" "B" "C" on each bottle,
• A for Armor Vitamins
• B for BCAA
• C for Carnitine/Creatine Complex
• ABC Essential Series

```html
<!DOCTYPE html>
<html lang="en">
<head>
<meta charset="utf-8">
<title>Roost Vector – Essential Series Labels</title>
<link rel="stylesheet" href="https://fonts.googleapis.com/css2?family=Audiowide&family=Exo+2:wght@400;600;800&display=swap">
<style>
  :root{
    --page:#ececec;
    --label-bg:#0b0b0c;
    --label-bg-2:#1b1b1e;
    --white:#ffffff;
    --ink:#111111;
    --red:#d01a2a;
    --red-deep:#6e0c14;
    --yellow:#d8df1c;
    --yellow-deep:#5d600a;
    --magenta:#c0279f;
    --magenta-soft:#e77ad2;
    --magenta-deep:#4a1040;
    --title-font:"Audiowide", sans-serif;
    --body-font:"Exo 2", sans-serif;
  }
  *{box-sizing:border-box;margin:0;padding:0}
  html,body{width:1200px;height:919px;overflow:hidden}
  body{
    background:var(--page);
    display:flex;align-items:center;justify-content:center;gap:24px;
    font-family:var(--body-font);
  }
  .label{
    position:relative;width:372px;height:234px;overflow:hidden;
    background:radial-gradient(ellipse at 50% 45%, var(--label-bg-2) 0%, var(--label-bg) 75%);
    color:var(--white);
  }
  .label--red{--accent:var(--red);--accent-deep:var(--red-deep)}
  .label--yellow{--accent:var(--yellow);--accent-deep:var(--yellow-deep)}
  .label--magenta{--accent:var(--magenta);--accent-deep:var(--magenta-deep)}

  .label__top-bar{position:absolute;left:0;top:0;width:100%;height:4px;background:var(--accent)}
  .label__bottom-bar{position:absolute;left:0;bottom:0;width:100%;height:6px;background:var(--accent)}

  .brand-tab{
    position:absolute;left:50%;top:0;transform:translateX(-50%);
    width:132px;height:27px;background:var(--accent);
    clip-path:polygon(0 0,100% 0,88% 100%,12% 100%);
    display:flex;align-items:center;justify-content:center;
  }
  .brand-tab__name{font-family:var(--body-font);font-weight:800;font-size:11.5px;letter-spacing:.3px;color:var(--white);text-transform:uppercase}
  .label--yellow .brand-tab__name{color:var(--ink)}

  .count-tab{
    position:absolute;left:50%;bottom:6px;transform:translateX(-50%);
    width:96px;height:15px;background:var(--accent);
    clip-path:polygon(10% 0,90% 0,100% 100%,0 100%);
    display:flex;align-items:center;justify-content:center;
    font-weight:800;font-size:7.5px;letter-spacing:.2px;color:var(--white);
  }
  .label--yellow .count-tab{color:var(--ink)}

  .title{
    position:absolute;left:0;width:100%;text-align:center;
    font-family:var(--title-font);text-transform:uppercase;
  }
  .title--creatine{top:52px;font-size:18.5px;color:var(--red);text-shadow:0 0 6px rgba(208,26,42,.5)}
  .title--bcaa{top:50px;font-size:27px;color:#fbffd6;text-shadow:0 0 8px var(--yellow),0 0 16px rgba(216,223,28,.6)}
  .title--vitamins{top:52px;font-size:27px;color:var(--magenta-soft);text-shadow:0 0 8px rgba(192,39,159,.7)}

  .title-glow{
    position:absolute;left:60px;top:44px;width:250px;height:40px;
    background:radial-gradient(ellipse at 40% 50%, rgba(190,40,30,.55) 0%, rgba(120,20,10,.2) 55%, transparent 80%);
  }

  .subtitle{
    position:absolute;top:88px;left:0;width:100%;text-align:center;
    font-weight:600;font-size:10.5px;line-height:13px;color:var(--white);
  }

  .emblem{
    position:absolute;display:flex;flex-direction:column;align-items:center;gap:3px;
  }
  .emblem__dot{width:22px;height:22px;border-radius:50%;background:var(--accent)}
  .emblem__name{font-family:var(--body-font);font-weight:800;font-size:7px;color:var(--white);text-transform:uppercase;white-space:nowrap}

  .hex{
    position:absolute;width:22px;height:24px;background:var(--accent);
    clip-path:polygon(50% 0,100% 25%,100% 75%,50% 100%,0 75%,0 25%);
    display:flex;align-items:center;justify-content:center;
  }
  .hex svg{width:13px;height:13px}

  .benefit{
    position:absolute;height:18px;display:flex;align-items:center;
    font-size:7px;line-height:8px;color:var(--white);padding:0 6px;
  }
  .benefit--left{justify-content:flex-start;background:linear-gradient(90deg,transparent,var(--accent-deep) 35%,var(--accent-deep))}
  .benefit--right{justify-content:flex-end;text-align:right;background:linear-gradient(270deg,transparent,var(--accent-deep) 35%,var(--accent-deep))}
  .label--yellow .benefit{height:20px;font-size:6.4px}

  .claim-band{
    position:absolute;left:40px;top:150px;width:292px;height:50px;
    background:linear-gradient(90deg,transparent,var(--magenta-deep) 20%,var(--magenta-deep) 80%,transparent);
    display:flex;align-items:center;justify-content:center;text-align:center;
    font-weight:600;font-size:11px;line-height:13px;color:var(--white);
  }
</style>
</head>
<body>

<!-- Bottle A: Creatine + Carnitine -->
<section class="label label--red">
  <div class="label__top-bar"></div>
  <div class="brand-tab"><span class="brand-tab__name">Roost Vector</span></div>
  <div class="title-glow" role="img" aria-label="Red smoky flame texture behind the product name"></div>
  <h2 class="title title--creatine">Creatine+Carnitine</h2>
  <p class="subtitle">Performance Enhancing<br>Supplements for Racing Pigeons</p>

  <div class="benefit benefit--left" style="left:70px;top:140px;width:96px">increase<br>endurance</div>
  <div class="hex" style="left:166px;top:137px">
    <svg viewBox="0 0 16 16"><path d="M8 14 2 8a3.2 3.2 0 0 1 6-3.5A3.2 3.2 0 0 1 14 8z" fill="none" stroke="#111" stroke-width="1.6"/><path d="M3 8h3l1-2 2 4 1-2h3" fill="none" stroke="#111" stroke-width="1.2"/></svg>
  </div>
  <div class="emblem" style="left:163px;top:134px;width:46px;margin-left:0;left:163px"></div>
  <div class="emblem" style="left:186px;top:132px;width:0"></div>
  <div class="emblem" style="left:163px;top:132px;width:46px"></div>
  <div class="emblem" style="left:190px;top:133px"><div class="emblem__dot"></div><span class="emblem__name">Roost Vector</span></div>
  <div class="hex" style="left:250px;top:137px">
    <svg viewBox="0 0 16 16"><path d="M8 1c1 3 5 5 5 9a5 5 0 0 1-10 0c0-2 1-3 2-4 0 2 1 3 2 3-1-3 0-6 1-8z" fill="#111"/></svg>
  </div>
  <div class="benefit benefit--right" style="left:272px;top:140px;width:70px">burn fat</div>

  <div class="benefit benefit--left" style="left:85px;top:177px;width:100px">build muscle</div>
  <div class="hex" style="left:186px;top:174px">
    <svg viewBox="0 0 16 16"><rect x="1" y="6" width="2" height="4" fill="#111"/><rect x="3" y="4" width="2" height="8" fill="#111"/><rect x="5" y="7" width="6" height="2" fill="#111"/><rect x="11" y="4" width="2" height="8" fill="#111"/><rect x="13" y="6" width="2" height="4" fill="#111"/></svg>
  </div>
  <div class="hex" style="left:230px;top:174px">
    <svg viewBox="0 0 16 16"><path d="M13 8a5 5 0 1 1-2-4" fill="none" stroke="#111" stroke-width="1.8"/><path d="M9 2h3.5v3.5z" fill="#111"/><path d="M8 6v4M6 8h4" stroke="#111" stroke-width="1.6"/></svg>
  </div>
  <div class="benefit benefit--right" style="left:252px;top:177px;width:72px">recover faster</div>

  <div class="count-tab">240 CAPSULES</div>
  <div class="label__bottom-bar"></div>
</section>

<!-- Bottle B: BCAA -->
<section class="label label--yellow">
  <div class="label__top-bar"></div>
  <div class="brand-tab"><span class="brand-tab__name">Roost Vector</span></div>
  <h2 class="title title--bcaa">BCAA</h2>

  <div class="benefit benefit--left" style="left:20px;top:103px;width:114px">support muscle<br>protein synthesis</div>
  <div class="hex" style="left:134px;top:101px">
    <svg viewBox="0 0 16 16"><rect x="1" y="6" width="2" height="4" fill="#111"/><rect x="3" y="4" width="2" height="8" fill="#111"/><rect x="5" y="7" width="6" height="2" fill="#111"/><rect x="11" y="4" width="2" height="8" fill="#111"/><rect x="13" y="6" width="2" height="4" fill="#111"/></svg>
  </div>
  <div class="benefit benefit--left" style="left:20px;top:137px;width:114px">decrease protein<br>catabolism</div>
  <div class="hex" style="left:134px;top:135px">
    <svg viewBox="0 0 16 16"><path d="M8 2v10M4 8l4 5 4-5" fill="none" stroke="#111" stroke-width="2"/></svg>
  </div>
  <div class="benefit benefit--left" style="left:20px;top:171px;width:114px">enhanced recovery<br>from exercise</div>
  <div class="hex" style="left:134px;top:169px">
    <svg viewBox="0 0 16 16"><path d="M13 8a5 5 0 1 1-2-4" fill="none" stroke="#111" stroke-width="1.8"/><path d="M9 2h3.5v3.5z" fill="#111"/><path d="M8 6v4M6 8h4" stroke="#111" stroke-width="1.6"/></svg>
  </div>

  <div class="emblem" style="left:166px;top:135px"><div class="emblem__dot"></div><span class="emblem__name">Roost Vector</span></div>

  <div class="hex" style="left:214px;top:101px">
    <svg viewBox="0 0 16 16"><circle cx="8" cy="8" r="2.2" fill="#111"/><circle cx="3" cy="3" r="1.6" fill="#111"/><circle cx="13" cy="3" r="1.6" fill="#111"/><circle cx="3" cy="13" r="1.6" fill="#111"/><circle cx="13" cy="13" r="1.6" fill="#111"/><path d="M3 3l10 10M13 3 3 13" stroke="#111" stroke-width="1"/></svg>
  </div>
  <div class="benefit benefit--right" style="left:236px;top:103px;width:118px;justify-content:flex-start;text-align:left;background:linear-gradient(90deg,var(--accent-deep),var(--accent-deep) 65%,transparent)">promote insulin<br>sensitivity</div>
  <div class="hex" style="left:214px;top:135px">
    <svg viewBox="0 0 16 16"><rect x="1" y="6" width="2" height="4" fill="#111"/><rect x="3" y="4" width="2" height="8" fill="#111"/><rect x="5" y="7" width="6" height="2" fill="#111"/><rect x="11" y="4" width="2" height="8" fill="#111"/><rect x="13" y="6" width="2" height="4" fill="#111"/></svg>
  </div>
  <div class="benefit benefit--right" style="left:236px;top:137px;width:126px;justify-content:flex-start;text-align:left;background:linear-gradient(90deg,var(--accent-deep),var(--accent-deep) 65%,transparent)">offset muscle breakdown and<br>increase muscular endurance</div>
  <div class="hex" style="left:214px;top:169px">
    <svg viewBox="0 0 16 16"><path d="M8 14V4M4 8l4-5 4 5" fill="none" stroke="#111" stroke-width="2"/></svg>
  </div>
  <div class="benefit benefit--right" style="left:236px;top:169px;width:132px;height:24px;justify-content:flex-start;text-align:left;background:linear-gradient(90deg,var(--accent-deep),var(--accent-deep) 65%,transparent)">promote lowered body fat levels,<br>increased strength, &amp; improves<br>muscle repair</div>

  <div class="count-tab">240 CAPSULES</div>
  <div class="label__bottom-bar"></div>
</section>

<!-- Bottle C: Vitamins -->
<section class="label label--magenta">
  <div class="label__top-bar"></div>
  <div class="brand-tab"><span class="brand-tab__name">Roost Vector</span></div>
  <h2 class="title title--vitamins">Vitamins</h2>
  <div class="emblem" style="left:164px;top:100px"><div class="emblem__dot" style="width:30px;height:30px"></div><span class="emblem__name">Roost Vector</span></div>
  <p class="claim-band">Supports Rigorous Training and<br>Needs To Support Growth and<br>Overall Well-being</p>
  <div class="count-tab">240 CAPSULES</div>
  <div class="label__bottom-bar"></div>
</section>

</body>
</html>
```